Design a double sided business card

We are looking for a clean, eye-catching, and contemporary design that enhances the brand and presents a premium, professional image. Our preference is for a brown card with black gloss detailing and embossed elements; however, we are open to creative input and design suggestions that best achieve a strong visual impact.

Please see the attached existing business card for reference. We use both black and brown colours consistently across our branding.

On sample provided

```html
<!DOCTYPE html>
<html lang="en">
<head>
<meta charset="utf-8">
<title>HALDEN business card</title>
<link rel="stylesheet" href="https://fonts.googleapis.com/css2?family=Montserrat:wght@400;600;700&display=swap">
<style>
  :root {
    --ink: #000000;
    --sand: #cbb69b;
    --backdrop: #e6e6e6;
  }
  * { margin: 0; padding: 0; box-sizing: border-box; }
  html, body { width: 1200px; height: 849px; overflow: hidden; }
  body {
    background: var(--backdrop);
    font-family: "Montserrat", sans-serif;
    color: var(--sand);
    position: relative;
  }
  .card {
    position: absolute;
    left: 320px;
    width: 560px;
    height: 320px;
    background: var(--ink);
    overflow: hidden;
  }
  .card--front { top: 84px; }
  .card--back { top: 444px; }

  .edge-tab {
    position: absolute;
    top: 108px;
    width: 32px;
    height: 104px;
    background: var(--sand);
    border-radius: 8px;
  }
  .edge-tab--left { left: -16px; }
  .edge-tab--right { right: -16px; }

  .base-band { position: absolute; left: 0; top: 0; width: 560px; height: 320px; }
  .base-band polygon { fill: var(--sand); }

  .brand-square {
    position: absolute;
    left: 240px;
    top: 92px;
    width: 80px;
    height: 80px;
    border: 6px solid var(--sand);
  }
  .brand-name {
    position: absolute;
    left: 0;
    width: 100%;
    top: 196px;
    text-align: center;
    font-weight: 700;
    font-size: 38px;
    letter-spacing: 8px;
    line-height: 1;
  }

  .holder { position: absolute; left: 31px; top: 16px; }
  .holder-name {
    font-weight: 600;
    font-size: 26px;
    line-height: 1.05;
    text-decoration: underline;
    text-decoration-thickness: 2px;
    text-underline-offset: 3px;
  }
  .holder-role {
    font-size: 12px;
    letter-spacing: 7.6px;
    line-height: 1.2;
    margin-top: 1px;
  }

  .contact-list { position: absolute; left: 31px; top: 84px; list-style: none; }
  .contact-item {
    display: flex;
    align-items: flex-start;
    font-size: 13px;
    line-height: 18px;
    margin-bottom: 11px;
  }
  .contact-item svg { width: 15px; height: 15px; margin: 1.5px 9px 0 0; flex: none; }
  .contact-item .dot { fill: var(--sand); }
  .contact-item .glyph { fill: var(--ink); stroke: var(--ink); }

  .brand-block {
    position: absolute;
    left: 345px;
    top: 76px;
    width: 135px;
    height: 134px;
    background: var(--sand);
    display: flex;
    align-items: center;
    justify-content: center;
    color: var(--ink);
    font-weight: 700;
    font-size: 21px;
    letter-spacing: 3px;
  }
</style>
</head>
<body>

<section class="card card--front" aria-label="Card front">
  <span class="edge-tab edge-tab--left"></span>
  <span class="edge-tab edge-tab--right"></span>
  <span class="brand-square"></span>
  <div class="brand-name">HALDEN</div>
  <svg class="base-band" viewBox="0 0 560 320" aria-hidden="true">
    <polygon points="27,291 261,291 279,309 27,309"/>
    <polygon points="273,291 532,291 532,309 291,309"/>
  </svg>
</section>

<section class="card card--back" aria-label="Card back">
  <div class="holder">
    <div class="holder-name">Ravi Kandola</div>
    <div class="holder-role">DIRECTOR</div>
  </div>

  <ul class="contact-list">
    <li class="contact-item">
      <svg viewBox="0 0 16 16" aria-hidden="true"><circle class="dot" cx="8" cy="8" r="8"/><path class="glyph" d="M5 4.2l1.6-.4 1 2.2-1 .8c.5 1.1 1.3 1.9 2.4 2.4l.8-1 2.2 1-.4 1.6c-3.6.2-6.8-3-6.6-6.6z" stroke-width="0"/></svg>
      0800 214 7730
    </li>
    <li class="contact-item">
      <svg viewBox="0 0 16 16" aria-hidden="true"><circle class="dot" cx="8" cy="8" r="8"/><rect class="glyph" x="5.6" y="3.8" width="4.8" height="8.4" rx="1" fill="none" stroke-width="1.3"/></svg>
      07700900416
    </li>
    <li class="contact-item">
      <svg viewBox="0 0 16 16" aria-hidden="true"><circle class="dot" cx="8" cy="8" r="8"/><rect class="glyph" x="4" y="5.2" width="8" height="5.6" stroke-width="0"/><path d="M4 5.4l4 3 4-3" fill="none" stroke="#cbb69b" stroke-width="0.9"/></svg>
      ravi@halden.co.uk
    </li>
    <li class="contact-item">
      <svg viewBox="0 0 16 16" aria-hidden="true"><circle class="dot" cx="8" cy="8" r="8"/><g class="glyph" fill="none" stroke-width="0.9"><circle cx="8" cy="8" r="4"/><ellipse cx="8" cy="8" rx="1.8" ry="4"/><path d="M4 8h8"/></g></svg>
      www.halden.co.uk
    </li>
    <li class="contact-item">
      <svg viewBox="0 0 16 16" aria-hidden="true"><circle class="dot" cx="8" cy="8" r="8"/><path class="glyph" d="M8 12.6c-2-2.3-3-3.9-3-5.2a3 3 0 0 1 6 0c0 1.3-1 2.9-3 5.2z" stroke-width="0"/><circle cx="8" cy="7.3" r="1.1" fill="#cbb69b"/></svg>
      <span>The Green Mill Lane<br>Eastbridge EB4 2QT</span>
    </li>
  </ul>

  <div class="brand-block">HALDEN</div>

  <svg class="base-band" viewBox="0 0 560 320" aria-hidden="true">
    <polygon points="27,279 289,279 274,297 27,297"/>
    <polygon points="301,279 532,279 532,297 286,297"/>
  </svg>
</section>

</body>
</html>
```